BrewHarbor coffee packaging design

We need a vector design (AI) for the printing of our coffee bags.

The bags are double sided. Front will be simple with logo and web address. Back will have lots of information (below) and the wording can be changed to suit if required.

Actual bag dimensions are: 240mm wide x 335mm high (each side) artwork should be inside those sizes.

Front:
Requires - BrewHarbor cup logo, web address (brewharbor.com.au) in lowercase Papyrus font and the words BREW HARBOR in uppercase.
**added** The front will also need a 90mm x 35mm no artwork area so we can place a sticker.

Back:
1.
Silver Kettle Logo (needs to be entire unmodified logo) and the tagline of "Overall winner of Australia's biggest coffee roasting competition"

2.
BrewHarbor is a family business, proudly Australian owned and operated. We strive to provide amazing coffee, excellent service and great value to all our customers.

3.
Our coffee is fresh roasted to order and shipped same day.

4.
50c from every kilogram sold goes directly to projects in coffee growing regions. TrueShare is the Kindest Deal of all - see: trueshare.net

Logos are attached and higher resolution ones are available if needed.

Industry/Entity Type

Business

Requirements
Must have
• Per the description, BrewHarbor logo and webaddress on the front and Silver Kettle logo on the back are required.

```html
<!DOCTYPE html>
<html lang="en">
<head>
<meta charset="utf-8">
<title>BrewHarbor Coffee Bag – Back</title>
<link rel="stylesheet" href="https://fonts.googleapis.com/css2?family=Josefin+Sans:wght@300;400;600&family=Josefin+Slab:wght@400&display=swap">
<style>
  :root {
    --backdrop: #efefef;
    --bag: #3a0d10;
    --bag-deep: #2c080b;
    --label: #ffffff;
    --label-green: #3d9a2e;
    --ink: #5a5a5a;
    --ink-soft: #7a7a7a;
    --rule: #9a9a9a;
    --ribbon-text: #ffffff;
  }
  * { box-sizing: border-box; margin: 0; padding: 0; }
  html, body { width: 1200px; height: 900px; overflow: hidden; }
  body {
    background: var(--backdrop);
    font-family: "Josefin Sans", sans-serif;
    color: var(--ink);
    position: relative;
  }
  .bag {
    position: absolute;
    left: 428px; top: 124px;
    width: 368px; height: 608px;
  }
  .bag-surface { position: absolute; inset: 0; }
  .label {
    position: absolute;
    left: 484px; top: 338px;
    width: 308px; height: 330px;
    border-radius: 50%;
    background: var(--label);
    border: 7px solid var(--label-green);
  }
  .label-item {
    position: absolute;
    left: 476px; width: 308px;
    text-align: center;
    text-transform: uppercase;
    white-space: nowrap;
  }
  .product-name {
    top: 383px;
    font-size: 7px;
    letter-spacing: 0.3px;
    color: var(--ink);
  }
  .product-name span { display: inline-flex; align-items: center; gap: 6px; }
  .product-name span::before, .product-name span::after {
    content: ""; width: 48px; height: 1px; background: var(--rule);
  }
  .award {
    top: 398px;
    font-family: "Josefin Slab", serif;
    font-weight: 400;
    font-size: 8.8px;
    line-height: 14px;
    letter-spacing: 0.2px;
    color: var(--ink);
  }
  .rule {
    position: absolute;
    height: 1px;
    background: var(--rule);
  }
  .rule-1 { left: 515px; width: 202px; top: 441px; }
  .rule-2 { left: 516px; width: 214px; top: 498px; }
  .rule-3 { left: 516px; width: 214px; top: 534px; }
  .rule-4 { left: 542px; width: 164px; top: 592px; }
  .copy {
    font-size: 6px;
    line-height: 12px;
    letter-spacing: 0.2px;
    color: var(--ink-soft);
    font-weight: 300;
  }
  .copy-about { top: 448px; }
  .copy-roast { top: 507px; }
  .copy-share { top: 543px; }
  .partners {
    position: absolute;
    left: 584px; top: 602px;
    width: 78px;
    display: flex; justify-content: space-between; align-items: center;
  }
  .partner {
    display: flex; flex-direction: column; align-items: center; gap: 2px;
    font-size: 5px; color: var(--ink); font-weight: 400;
  }
  .partner-dot { width: 14px; height: 14px; border-radius: 50%; background: var(--ink); }
  .ribbon {
    position: absolute;
    left: 569px; top: 639px;
    width: 144px; height: 17px;
    background: var(--label-green);
    color: var(--ribbon-text);
    font-size: 7.5px; font-weight: 600;
    letter-spacing: 0.4px;
    display: flex; align-items: center; justify-content: center; gap: 6px;
    text-transform: uppercase;
  }
  .ribbon::before, .ribbon::after {
    content: ""; width: 14px; height: 1px; background: var(--ribbon-text);
  }
</style>
</head>
<body>
  <div class="bag">
    <svg class="bag-surface" width="368" height="608" viewBox="0 0 368 608" role="img" aria-label="Deep maroon bag surface with a fine repeating coffee-bean pattern">
      <defs>
        <linearGradient id="bagShade" x1="0" y1="0" x2="1" y2="0">
          <stop offset="0" stop-color="#2c080b"/>
          <stop offset="0.5" stop-color="#3a0d10"/>
          <stop offset="1" stop-color="#2c080b"/>
        </linearGradient>
      </defs>
      <rect width="368" height="608" fill="url(#bagShade)"/>
    </svg>
  </div>

  <div class="label"></div>

  <p class="label-item product-name"><span>Black Coffee</span></p>
  <h1 class="label-item award">Overall winner of Australia’s<br>biggest coffee roasting<br>competition</h1>
  <div class="rule rule-1"></div>
  <p class="label-item copy copy-about">BrewHarbor is a family business, proudly<br>Australian owned and operated. We strive to<br>provide amazing coffee, excellent service and<br>great value to all our customers.</p>
  <div class="rule rule-2"></div>
  <p class="label-item copy copy-roast">Our coffee is fresh roasted to order and<br>shipped same day.</p>
  <div class="rule rule-3"></div>
  <p class="label-item copy copy-share">50c from every kilogram sold goes directly<br>to projects in coffee growing regions.<br>TrueShare is the Kindest Deal of<br>all - see: trueshare.net</p>
  <div class="rule rule-4"></div>

  <div class="partners">
    <div class="partner"><span class="partner-dot"></span><span>TrueShare</span></div>
    <div class="partner"><span class="partner-dot"></span><span>Silver Kettle</span></div>
  </div>

  <div class="ribbon">Net wt. 12 oz.</div>
</body>
</html>
```